New high end server provider needs wordpress design

www.kv7hosting.com

Need a wordpress design for a high end server provider that provides overclocked dedicated servers for rent. We are located in Chicago but we have a presence is Virginia and Nevada for both our east and west coast customers.

We are a server provider that specializes in top end hardware with every feature designed for optimum performance. If it is not the best quality part or provides the best possible performance we don't run it. Our customers are mainly those that want the best single threaded performance possible from their hardware. We would be selling our services directly on our website via WHMCS.

We would like to see designs that are very modern and simplistic yet very attractive looking and catchy. Would prefer colors in the blues and greens and white. These colors are not necessary and I would be open to another color scheme if it looks good.

The final design should show speed and performance while being simplistic and easy on the eyes.

Logo and company name added and payment changed to guaranteed.  Looking for a wordpress template with the same pages as kv7hosting.com but with a redesigned look and feel.  

WHMCS control panel design also part of the design request.

If you have any questions please let me know!  This is just for kv7hosting.com and a main page for WHMCS (no coding just design).

Target Market(s)

IT Guru's (mostly men in their 20's to 30's)

Industry/Entity Type

Hardware

Requirements
Must have
• WHMCS panel design to fit with website theme.
Nice to have
• Main slider on home page similar to one of our other websites at www.kv7hosting.com
Should not have
• Flash or frames

```html
<!DOCTYPE html>
<html lang="en">
<head>
<meta charset="utf-8">
<title>KV7Hosting – High End Dedicated Servers</title>
<link rel="stylesheet" href="https://fonts.googleapis.com/css2?family=Oswald:wght@400;500&family=Open+Sans:wght@400;600;700&family=PT+Sans:wght@400;700&display=swap">
<style>
:root{
  --ink:#1d1d1d;
  --body:#333;
  --line:#e2e2e2;
  --hero-top:#0c3150;
  --hero-mid:#1b6a98;
  --hero-glow:#7cc8ea;
  --slider-bar:#0d1620;
  --accent:#ffd21f;
  --btn-top:#2a7bb8;
  --btn-bottom:#0d4f86;
  --footer:#0e2232;
  --footer-deep:#0a1824;
  --footer-link:#9fb1bf;
}
*{margin:0;padding:0;box-sizing:border-box}
html,body{width:685px;height:1200px;overflow:hidden;background:#fff}
body{position:relative;font-family:"Open Sans",Arial,sans-serif;color:var(--body)}
.site-header{position:absolute;top:0;left:0;width:685px;height:48px;background:#fff;border-bottom:1px solid var(--line)}
.brand{position:absolute;left:69px;top:12px;display:flex;align-items:center;gap:6px;font-family:"Oswald",sans-serif;font-weight:500;font-size:18px;color:var(--slider-bar);letter-spacing:.5px}
.brand-dot{width:14px;height:14px;border-radius:50%;background:var(--slider-bar)}
.main-nav{position:absolute;left:233px;top:19px;display:flex;gap:17px;font-size:8.5px;color:#444;text-transform:uppercase;letter-spacing:.2px}
.nav-pointer{position:absolute;left:122px;top:48px;width:0;height:0;border-left:6px solid transparent;border-right:6px solid transparent;border-top:6px solid #fff;z-index:3}
.hero{position:absolute;top:48px;left:0;width:685px;height:292px;background:radial-gradient(ellipse 520px 150px at 342px 260px,var(--hero-glow) 0%,var(--hero-mid) 45%,var(--hero-top) 85%)}
.hero-kicker{position:absolute;top:52px;width:100%;text-align:center;font-size:7px;letter-spacing:4px;color:#bfe0f2}
.hero-title{position:absolute;top:64px;width:100%;text-align:center;font-family:"PT Sans",sans-serif;font-weight:700;font-size:30px;color:#fff;letter-spacing:-.5px}
.hero-sub{position:absolute;top:99px;width:100%;text-align:center;font-family:"PT Sans",sans-serif;font-size:15px;color:#fff}
.hero-sub b{font-weight:700}
.hero-sub .price-old{color:#cfe3ee}
.hero-sub .price-new{color:var(--accent);font-weight:700}
.hero-server{position:absolute;left:160px;top:190px;width:365px;height:102px;background:linear-gradient(#3a3f44,#15181b);border-radius:3px}
.slider-bar{position:absolute;left:57px;top:307px;width:570px;height:66px;background:var(--slider-bar);color:#fff;text-align:center}
.slider-title{margin-top:12px;font-family:"Oswald",sans-serif;font-size:20px;letter-spacing:.5px}
.slider-text{font-size:7px;color:#d5dde3;margin-top:3px}
.slider-arrow{position:absolute;top:21px;width:24px;height:24px}
.slider-arrow.prev{left:15px}.slider-arrow.next{right:15px}
.section{position:absolute;left:59px;width:570px}
.section h2{font-family:"Oswald",sans-serif;font-weight:400;font-size:24px;color:var(--ink)}
.section p{font-size:8.3px;line-height:12.6px;color:#333}
.welcome{top:404px}
.welcome-map{position:absolute;left:260px;top:392px;width:360px;height:170px;background:radial-gradient(ellipse at center,#f0f1f2 0%,#fff 70%)}
.offer{top:578px}
.plans{position:absolute;left:57px;top:677px;width:571px;height:272px;border:1px solid var(--line);box-shadow:0 2px 8px rgba(0,0,0,.12);display:flex;background:#fff}
.plan{flex:1;border-right:1px solid var(--line);position:relative}
.plan:last-child{border-right:0}
.plan h3{font-family:"Oswald",sans-serif;font-weight:400;font-size:15px;color:var(--ink);padding:11px 0 0 12px;height:42px;text-transform:uppercase}
.plan-visual{height:72px;background:linear-gradient(#f7f9fb,#e9eef2);position:relative}
.plan-visual .shape{position:absolute;left:50%;top:8px;transform:translateX(-50%);width:86px;height:60px;background:linear-gradient(#6b7177,#2b2f33);border-radius:3px}
.plan-badge{position:absolute;left:65px;top:8px;background:#fbe7b8;font-family:"Oswald",sans-serif;font-size:8px;color:#222;padding:3px 6px;line-height:1}
.plan-badge b{font-size:20px;font-weight:500}
.features{list-style:none;margin-top:6px}
.features li{height:27px;border-top:1px solid #ececec;font-size:7px;color:#333;display:flex;align-items:center;gap:12px;padding-left:12px}
.features li:first-child{border-top:0}
.plan-btn{position:absolute;left:20px;bottom:14px;width:150px;height:25px;background:linear-gradient(var(--btn-top),var(--btn-bottom));color:#fff;font-family:"Oswald",sans-serif;font-size:11px;text-align:center;line-height:25px;border-radius:2px;border-top:1px solid #1b5f98}
.partners{position:absolute;top:980px;left:215px;display:flex;gap:30px;align-items:center}
.partner{height:16px;background:#d8dadc;border-radius:2px}
.site-footer{position:absolute;top:1020px;left:0;width:685px;height:180px;background:linear-gradient(var(--footer),var(--footer-deep))}
.footer-brand{position:absolute;left:75px;top:68px;font-family:"Oswald",sans-serif;font-size:18px;color:#1e3a50;display:flex;gap:6px;align-items:center}
.footer-brand .dot{width:14px;height:14px;border-radius:50%;background:#1e3a50}
.footer-col{position:absolute;top:32px}
.footer-col h4{font-family:"Oswald",sans-serif;font-weight:400;font-size:10px;color:#fff;margin-bottom:4px;letter-spacing:.5px}
.footer-col a{display:block;font-size:6.5px;color:var(--footer-link);line-height:13px;text-decoration:none;text-transform:uppercase}
.connect{position:absolute;top:123px;left:157px;display:flex;align-items:center;gap:11px;font-family:"Oswald",sans-serif;font-size:9px;color:#fff;letter-spacing:.5px}
.social{width:8px;height:8px;border-radius:50%;background:#c7d3dc}
.newsletter{position:absolute;left:367px;top:121px;width:160px;height:16px;background:#13324a;border:1px solid #1d4460;font-size:6.5px;color:#6e8ba0;line-height:14px;padding-left:6px}
.newsletter svg{position:absolute;right:4px;top:3px}
.copyright{position:absolute;top:157px;width:100%;text-align:center;font-size:6.5px;color:#3d5a70}
</style>
</head>
<body>
<header class="site-header">
  <div class="brand"><span class="brand-dot"></span>KV7HOSTING</div>
  <nav class="main-nav"><span>Our Servers</span><span>Dedicated Servers</span><span>Why KV7?</span><span>Testimonials</span><span>FAQ's</span><span>Contacts</span></nav>
</header>
<div class="nav-pointer"></div>

<section class="hero">
  <div class="hero-kicker">SMART SERVER</div>
  <h1 class="hero-title">The best value server on the web.</h1>
  <div class="hero-sub"><b>Corevia Dual Vantix Quad Core</b> with <b>16GB RAM + 1TB Storage.</b> <span class="price-old">$319/mo</span> <span class="price-new">$209/mo</span></div>
  <div class="hero-server" role="img" aria-label="Rack-mounted server unit over a glowing planet horizon"></div>
</section>
<div class="slider-bar">
  <svg class="slider-arrow prev" viewBox="0 0 24 24"><circle cx="12" cy="12" r="11" fill="#2a2f35" stroke="#555"/><path d="M14 7l-5 5 5 5" fill="none" stroke="#fff" stroke-width="2"/></svg>
  <div class="slider-title">SPEEDS THAT SET US APART FROM THE COMPETITION</div>
  <div class="slider-text">Each server is given a dedicated CPU core with high priority access · Your server is the only thing that is running on that core.</div>
  <svg class="slider-arrow next" viewBox="0 0 24 24"><circle cx="12" cy="12" r="11" fill="#2a2f35" stroke="#555"/><path d="M10 7l5 5-5 5" fill="none" stroke="#fff" stroke-width="2"/></svg>
</div>

<div class="welcome-map" role="img" aria-label="Faint world map in the background"></div>
<section class="section welcome">
  <h2>Welcome</h2>
  <p style="margin-top:8px">KV7Hosting offer the highest quality, highest performing Frontier Assault 2 servers available for rent. Our servers are custom built specifically for the demanding requirements of Frontier Assault 2 Beta. Each Frontier Assault 2 game server is ran on a 4.4 Ghz overclocked Corevia core V5 2600x CPU, so you can be assured that our servers will be able to run at high tickrates with 20+ players.Unlike most game server providers, we offer unlimited player slots on all of our rentals. This means that you can increase the player count when the game becomes more optimized, ensuring that your server will always be one of the most popular and best performing Frontier Assault 2 servers around.</p>
  <p style="margin-top:12px">Interested in ordering? See our Pricing Page for more information.<br>Have any questions? We have multiple contact methods located on our Contacts Page</p>
</section>

<section class="section offer">
  <h2>What we offer?</h2>
  <p style="margin-top:1px">Lorem Ipsum is simply dummy text of the printing and typesetting industry. Lorem Ipsum has been the industry's standard dummy text ever since the 1500s, when an unknown printer took a galley of type and scrambled it to make a type specimen book. It has survived not only five centuries, but also the leap into electronic typesetting, remaining essentially unchanged. It was popularised in the 1960s with the release of Typeset Co. sheets containing Lorem Ipsum passages, and more recently with desktop publishing software like PageForge including versions of Lorem Ipsum.</p>
</section>

<div class="plans">
  <article class="plan">
    <h3>Game Servers Hosting</h3>
    <div class="plan-visual" role="img" aria-label="Rack server unit"><div class="shape" style="top:30px;height:24px;width:110px"></div><div class="plan-badge"><b>6</b> MONTHS<br>FREE</div></div>
    <ul class="features">
      <li><svg width="9" height="8" viewBox="0 0 9 8"><path d="M1 4l2.5 3L8 1" fill="none" stroke="#555" stroke-width="1.6"/></svg>Unlimited Storage</li>
      <li><svg width="9" height="8" viewBox="0 0 9 8"><path d="M1 4l2.5 3L8 1" fill="none" stroke="#555" stroke-width="1.6"/></svg>Unlimited Bandwidth</li>
      <li><svg width="9" height="8" viewBox="0 0 9 8"><path d="M1 4l2.5 3L8 1" fill="none" stroke="#555" stroke-width="1.6"/></svg>Unlimited Websites</li>
    </ul>
    <div class="plan-btn">PLAN &amp; PRICUNG</div>
  </article>
  <article class="plan">
    <h3>Dedicated Server Hosting</h3>
    <div class="plan-visual" role="img" aria-label="Tower server cases"><div class="shape" style="width:70px"></div></div>
    <ul class="features">
      <li><svg width="9" height="8" viewBox="0 0 9 8"><path d="M1 4l2.5 3L8 1" fill="none" stroke="#555" stroke-width="1.6"/></svg>Unlimited Storage</li>
      <li><svg width="9" height="8" viewBox="0 0 9 8"><path d="M1 4l2.5 3L8 1" fill="none" stroke="#555" stroke-width="1.6"/></svg>Unlimited Bandwidth</li>
      <li><svg width="9" height="8" viewBox="0 0 9 8"><path d="M1 4l2.5 3L8 1" fill="none" stroke="#555" stroke-width="1.6"/></svg>Unlimited Websites</li>
    </ul>
    <div class="plan-btn">PLAN &amp; PRICUNG</div>
  </article>
  <article class="plan">
    <h3>Server Administration.</h3>
    <div class="plan-visual" role="img" aria-label="Blade server chassis"><div class="shape" style="width:64px;height:64px;top:4px"></div></div>
    <ul class="features">
      <li><svg width="9" height="8" viewBox="0 0 9 8"><path d="M1 4l2.5 3L8 1" fill="none" stroke="#555" stroke-width="1.6"/></svg>Unlimited Storage</li>
      <li><svg width="9" height="8" viewBox="0 0 9 8"><path d="M1 4l2.5 3L8 1" fill="none" stroke="#555" stroke-width="1.6"/></svg>Unlimited Bandwidth</li>
      <li><svg width="9" height="8" viewBox="0 0 9 8"><path d="M1 4l2.5 3L8 1" fill="none" stroke="#555" stroke-width="1.6"/></svg>Unlimited Websites</li>
    </ul>
    <div class="plan-btn">PLAN &amp; PRICUNG</div>
  </article>
</div>

<div class="partners">
  <div class="partner" style="width:68px"></div>
  <div class="partner" style="width:34px;height:22px;border-radius:50%"></div>
  <div class="partner" style="width:70px"></div>
</div>

<footer class="site-footer">
  <div class="footer-brand"><span class="dot"></span>KV7HOSTING</div>
  <div class="footer-col" style="left:280px"><h4>ABOUT</h4><a>Locations</a><a>Team</a><a>Careers</a></div>
  <div class="footer-col" style="left:347px"><h4>WORK</h4><a>Portfolio</a><a>Services</a></div>
  <div class="footer-col" style="left:413px"><h4>BLOGS</h4><a>Advance</a><a>Inspire</a><a>Extend</a><a>Flourish</a></div>
  <div class="footer-col" style="left:484px"><h4>MORE</h4><a>Northwind Labs</a><a>Talkrate</a><a>Team Brightloop</a></div>
  <div class="footer-col" style="left:571px"><h4>CONTACT</h4><a>Send a Message</a><a>Find Us</a></div>
  <div class="connect">CONNECT WITH US : <span class="social"></span><span class="social"></span><span class="social"></span><span class="social"></span></div>
  <div class="newsletter">Enter email address<svg width="8" height="8" viewBox="0 0 8 8"><path d="M1 4h6M4 1l3 3-3 3" fill="none" stroke="#9fb1bf" stroke-width="1.2"/></svg></div>
  <div class="copyright">Copyright © 2013 KV7 Hosting. All Rights Reserved.</div>
</footer>
</body>
</html>
```